Harrowgate Estates Business Card for Apartment Buildings

Create business cards for resident managers who run apartment buildings. The audience is the public who are searching for apartment rentals, and current residents who live at the apartment building. Key design element will be incorporating the company logo, however, the logo cannot dominate. The building name and manager name are more important than the logo. Current business card design leaves little room for copy, so we may need to reduce the size on the current card to allow for more space for copy.

Target Market(s)

Adults 18-65 years of age, who are looking for an apartment rental, plus current residents who live at our apartment buildings.

Industry/Entity Type

Property Management

Contact Information for Business Card

A major design element will be use of the company logo. Important property and manager contact information must be part of the design. The size of the logo will need to be reduced to make room for building and manager contact copy.

Font styles to use
Sans Serif

Colors
3176b5
000000
959595
ffffff

Requirements
Must have
• 1) Incorporate the company logo.
• 2) Use the company colors (dark blue, black/grey, over white).
• 3) FEATURE THE BUILDING NAME
• 4) FEATURE THE MANAGER NAME
• 5) The company name is less important than BUILDING and MANAGER
• 6) Manager contact information
• **SEE ATTACHED CREATIVE BRIEF**
Nice to have
• 1) Back of card logo watermark
• 2) Ability to write notes on back of carfd
Should not have
• Avoid letting the company logo dominate the card, the building name and manager are more important than the company logo.

```html
<!DOCTYPE html>
<html lang="en">
<head>
<meta charset="utf-8">
<title>Harrowgate Estates – Resident Manager Card</title>
<link rel="stylesheet" href="https://fonts.googleapis.com/css2?family=Arimo:ital,wght@0,400;0,700;1,700&display=swap">
<style>
  :root {
    --brand-blue: #1a3fd6;
    --icon-blue: #2238d8;
    --card-black: #000000;
    --panel-grey: #8c9b9b;
    --panel-edge: #e9eeee;
    --paper: #ffffff;
    --rule: #5d6466;
    --ink: #000000;
    --watermark: #dfe6f3;
  }
  * { box-sizing: border-box; margin: 0; padding: 0; }
  html, body {
    width: 914px; height: 1200px; overflow: hidden;
    background: var(--paper);
    font-family: "Arimo", Arial, sans-serif;
  }
  .canvas { position: relative; width: 914px; height: 1200px; }

  .card { position: absolute; left: 29px; width: 859px; background: var(--card-black); }
  .card--front { top: 29px; height: 515px; }
  .card--back { top: 659px; height: 516px; }

  /* company name, set vertically */
  .company {
    position: absolute; left: 108px; top: 460px;
    transform: rotate(-90deg); transform-origin: left top;
    display: flex; align-items: center; gap: 14px;
    color: var(--paper); font-weight: 700; font-size: 36px;
    letter-spacing: 1px; white-space: nowrap;
  }
  .company__mark { width: 28px; height: 28px; background: var(--brand-blue); }

  .info-panel {
    position: absolute; left: 218px; top: 54px; width: 584px; height: 404px;
    background: var(--panel-grey); border: 3px solid var(--panel-edge);
    text-align: right; padding: 12px 20px 0 0;
  }
  .manager-name {
    font-weight: 700; font-size: 46px; line-height: 1; letter-spacing: 1px;
    color: var(--brand-blue);
    -webkit-text-stroke: 6px var(--paper); paint-order: stroke fill;
  }
  .manager-title {
    font-weight: 700; font-style: italic; font-size: 30px; line-height: 1.1;
    color: var(--brand-blue); margin-top: 2px;
  }
  .building-name { font-weight: 700; font-size: 33px; line-height: 1.1; color: var(--ink); margin-top: 12px; }
  .address { font-weight: 700; font-size: 25px; line-height: 28px; color: var(--ink); margin-top: 2px; }

  .contact-list { list-style: none; margin-top: 26px; }
  .contact-list li {
    display: flex; justify-content: flex-end; align-items: center; gap: 4px;
    font-size: 28px; line-height: 32px; color: var(--ink);
  }
  .contact-list svg { width: 30px; height: 30px; flex: none; }

  .notes-panel {
    position: absolute; left: 56px; top: 58px; width: 745px; height: 401px;
    background: var(--paper); border: 3px solid #b9c2c2; overflow: hidden;
  }
  .notes-watermark {
    position: absolute; left: 70px; top: 196px;
    font-weight: 700; font-size: 64px; line-height: 1;
    color: var(--watermark); white-space: nowrap;
  }
  .notes-title {
    position: relative; text-align: center; font-weight: 700; font-size: 33px;
    line-height: 1; color: var(--brand-blue); margin-top: 6px;
  }
  .notes-lines {
    position: absolute; left: 12px; right: 12px; top: 30px;
    height: 350px;
    background: repeating-linear-gradient(to bottom, transparent 0 34px, var(--rule) 34px 35px);
  }
</style>
</head>
<body>
<div class="canvas">

  <section class="card card--front">
    <div class="company"><span class="company__mark"></span>Harrowgate Estates</div>

    <div class="info-panel">
      <h1 class="manager-name">MARISOL QUINTERO</h1>
      <p class="manager-title">Resident Manager</p>
      <h2 class="building-name">Juniper Court Apartments</h2>
      <p class="address">2845 Wexford Street<br>Brookhaven, CA 91234</p>

      <ul class="contact-list">
        <li>555-210-4418
          <svg viewBox="0 0 28 28" aria-label="office phone"><circle cx="14" cy="14" r="13" fill="var(--icon-blue)" stroke="#fff" stroke-width="1.5"/><path d="M7 12c0-3 14-3 14 0v2h-4v-2h-6v2H7z" fill="#fff"/><path d="M9 15h10l1 5H8z" fill="#fff"/><circle cx="14" cy="17.5" r="1.6" fill="var(--icon-blue)"/></svg></li>
        <li>555-384-2071
          <svg viewBox="0 0 28 28" aria-label="mobile phone"><circle cx="14" cy="14" r="13" fill="var(--icon-blue)" stroke="#fff" stroke-width="1.5"/><rect x="9.5" y="6" width="9" height="16" rx="1.5" fill="none" stroke="#fff" stroke-width="2"/><circle cx="14" cy="19" r="1" fill="#fff"/></svg></li>
        <li>555-662-9035
          <svg viewBox="0 0 28 28" aria-label="fax"><circle cx="14" cy="14" r="13" fill="var(--icon-blue)" stroke="#fff" stroke-width="1.5"/><rect x="10" y="6" width="8" height="5" fill="#fff"/><rect x="6" y="11" width="16" height="7" rx="1" fill="#fff"/><rect x="10" y="16" width="8" height="6" fill="#fff" stroke="var(--icon-blue)"/></svg></li>
        <li>marisol@harrowgate.com
          <svg viewBox="0 0 28 28" aria-label="email"><circle cx="14" cy="14" r="13" fill="var(--icon-blue)" stroke="#fff" stroke-width="1.5"/><rect x="7" y="9" width="14" height="10" fill="#fff"/><path d="M7 9l7 6 7-6M7 19l5-5M21 19l-5-5" fill="none" stroke="var(--icon-blue)" stroke-width="1.2"/></svg></li>
        <li>www.harrowgate.com
          <svg viewBox="0 0 28 28" aria-label="website"><circle cx="14" cy="14" r="13" fill="var(--icon-blue)" stroke="#fff" stroke-width="1.5"/><circle cx="14" cy="14" r="8" fill="none" stroke="#fff" stroke-width="1.6"/><ellipse cx="14" cy="14" rx="3.5" ry="8" fill="none" stroke="#fff" stroke-width="1.4"/><path d="M6 14h16" stroke="#fff" stroke-width="1.4"/></svg></li>
      </ul>
    </div>
  </section>

  <section class="card card--back">
    <div class="notes-panel">
      <div class="notes-watermark">Harrowgate Estates</div>
      <h2 class="notes-title">NOTES</h2>
      <div class="notes-lines"></div>
    </div>
  </section>

</div>
</body>
</html>
```